KTR Keystone Tally Resources Pty Ltd

Design a website for bookkeeping & accounting company

I like this website as an example with my own branding

https://go.lumiqor.example/sydney-bookkeeping-lp/?keyword=bookkeeping%20sydney&matchtype=e&campaignid=481726350&device=c&adgroupid=37215068492&adposition=1t1&creative=519384726105&gclid=XQzRbTpWvK7dLmN3FhJsYcGe4uA9oPiZ2wHqVxB_TkE

Number of Pages Required

1 page

Font styles to use
Sans Serif

Colors
9bcb3c

```html
<!DOCTYPE html>
<html lang="en">
<head>
<meta charset="utf-8">
<title>KTR Keystone Tally Resources – Bookkeeping</title>
<link rel="stylesheet" href="https://fonts.googleapis.com/css2?family=Montserrat:wght@400;500;600;700&display=swap">
<style>
:root{
  --mint:#80d3b6;
  --red:#ee1c1c;
  --green:#8cc63f;
  --navy:#1f3a93;
  --ink:#333333;
  --muted:#777777;
  --soft:#f4f4f4;
  --dark:#4a4a4a;
  --footer:#363636;
  --white:#ffffff;
}
*{margin:0;padding:0;box-sizing:border-box}
html,body{width:1200px;height:3982px;overflow:hidden}
body{font-family:'Montserrat',sans-serif;color:var(--ink);background:var(--white);position:relative}
section,header,footer{position:absolute;left:0;width:1200px}
.abs{position:absolute}
.btn{position:absolute;background:var(--red);color:var(--white);font-weight:600;display:flex;align-items:center;justify-content:center;border-radius:2px}

/* header */
.site-header{top:0;height:106px;background:linear-gradient(180deg,#2c3036,#1b1e22)}
.brand{left:85px;top:30px;color:var(--white);font-weight:600;display:flex;align-items:center;gap:14px}
.brand-mark{font-size:40px;letter-spacing:1px}
.brand-name{font-size:12px;line-height:14px;width:150px;border-left:1px solid rgba(255,255,255,.7);padding-left:10px}
.nav{left:690px;top:44px;display:flex;gap:26px;font-size:13px;color:var(--white);font-weight:500}
.nav .active{color:var(--green)}
.site-header .btn{left:985px;top:38px;width:128px;height:30px;font-size:12px}

/* hero */
.hero{top:106px;height:484px;background:var(--mint)}
.hero-art{left:133px;top:67px;width:305px;height:411px;border-radius:6px;background:linear-gradient(160deg,#9fe0c8,#6cc3a4)}
.hero h1{left:695px;top:78px;font-size:30px;font-weight:500;line-height:38px;color:#222}
.hero .lead{left:695px;top:178px;font-size:17px;line-height:22px;color:#222;width:360px}
.field{position:absolute;left:695px;width:388px;height:37px;background:var(--white);border-radius:3px;font-size:13px;color:#888;padding:11px 14px}
.hero .btn{left:695px;top:359px;width:388px;height:53px;font-size:16px}

/* intro */
.intro{top:590px;height:653px;background:var(--white)}
.intro h2{left:0;width:1200px;top:60px;text-align:center;font-size:31px;font-weight:500;line-height:42px;color:#444}
.feature{position:absolute;left:175px;width:400px;display:flex;gap:38px}
.feature-icon{width:80px;height:80px;border-radius:50%;background:#e3e3e3;flex:none;display:flex;align-items:center;justify-content:center}
.feature-icon.on{background:var(--mint)}
.feature h3{font-size:15px;font-weight:500;color:#555;margin-top:0;margin-bottom:10px}
.feature p{font-size:11.5px;line-height:19px;color:var(--muted);width:300px}
.intro-art{left:637px;top:193px;width:451px;height:425px;border-radius:50%;background:radial-gradient(circle,#fafafa,#e6e6e6)}

/* services */
.services{top:1243px;height:1080px;background:var(--soft)}
.services h2{left:0;width:1200px;top:102px;text-align:center;font-size:30px;font-weight:500;color:#444}
.rule{left:540px;top:150px;width:120px;height:2px;background:#bbb}
.service{position:absolute;width:300px;text-align:center}
.service svg{display:block;margin:0 auto 14px}
.service h3{font-size:15px;font-weight:500;color:#333;margin-bottom:12px}
.service p{font-size:11.5px;line-height:19px;color:#666}
.services .btn{left:516px;top:929px;width:238px;height:50px;font-size:16px}

/* cta */
.cta{top:2323px;height:266px;background:linear-gradient(90deg,#555,#3e3e3e)}
.cta h2{left:178px;top:60px;font-size:31px;font-weight:500;line-height:40px;color:var(--white);width:640px}
.cta p{left:178px;top:158px;font-size:12.5px;line-height:20px;color:#eee;width:580px}
.cta .btn{left:785px;top:140px;width:250px;height:50px;font-size:16px}

/* partners */
.partners{top:2589px;height:186px;background:var(--white)}
.partner{position:absolute;top:78px;width:150px;text-align:center;font-size:19px;font-weight:700;color:#333;display:flex;align-items:center;justify-content:center;gap:8px}
.partner .dot{width:20px;height:20px;border-radius:50%;background:#333}

/* testimonials */
.testimonials{top:2775px;height:536px;background:var(--soft)}
.testimonials h2{left:0;width:1200px;top:60px;text-align:center;font-size:26px;font-weight:600;color:#222}
.quote-card{left:152px;top:143px;width:460px;height:317px;background:var(--white)}
.avatar{left:43px;top:40px;width:90px;height:90px;border-radius:50%;background:linear-gradient(160deg,#d9cfc5,#9a8d82)}
.person{left:148px;top:62px}
.person .name{font-size:24px;font-weight:600;color:var(--green)}
.person .role{font-size:16px;font-weight:600;color:var(--navy)}
.quote-card p{left:58px;top:145px;width:375px;font-size:11px;line-height:18px;color:#666}
.video{left:612px;top:143px;width:400px;height:317px;background:linear-gradient(150deg,#4b5560,#1f252b)}
.video-title{left:10px;top:6px;color:var(--white);font-size:12px;font-weight:600}
.play{left:172px;top:130px}

/* contact */
.contact{top:3311px;height:534px;background:var(--mint)}
.map{left:85px;top:144px;width:472px;height:285px;background:linear-gradient(135deg,#eceae3,#d6e4d2);border:6px solid var(--white)}
.map-label{left:8px;top:8px;background:var(--white);font-size:11px;padding:6px 8px;color:#333;box-shadow:0 1px 3px rgba(0,0,0,.2)}
.contact h2{left:613px;top:155px;font-size:28px;font-weight:500;color:var(--white)}
.contact .intro-text{left:613px;top:203px;width:440px;font-size:11.5px;line-height:19px;color:var(--white)}
.row{position:absolute;left:613px;display:flex;font-size:13px;color:var(--white)}
.row .label{width:102px;font-weight:500}
.row .value{font-size:15px}
.social{display:flex;gap:20px}
.social span{width:16px;height:16px;border-radius:50%;background:var(--white)}

/* footer */
.site-footer{top:3845px;height:137px;background:var(--footer);color:#ddd;font-size:12px;text-align:center;padding-top:61px}
</style>
</head>
<body>

<header class="site-header">
  <div class="abs brand"><span class="brand-mark">KTR</span><span class="brand-name">Keystone Tally Resources Pty Ltd</span></div>
  <nav class="abs nav"><span class="active">HOME</span><span>SERVICES</span><span>ABOUT</span><span>CONTACT</span></nav>
  <a class="btn">Start A Free Trial</a>
</header>

<section class="hero">
  <div class="abs hero-art" role="img" aria-label="Illustration of a businessman at a laptop surrounded by finance icons"></div>
  <h1 class="abs">Free yourself With KTR<br>We'll do your Bookkeeping.</h1>
  <p class="abs lead">Australia's Largest Bookeeping service for small businesse</p>
  <div class="field" style="top:242px">Full Name</div>
  <div class="field" style="top:297px">Email</div>
  <a class="btn">Start Your Free Trial</a>
</section>

<section class="intro">
  <h2 class="abs">One of the largest bookkeeping<br>companies in Australia</h2>
  <div class="feature" style="top:195px">
    <div class="feature-icon on"><svg width="40" height="30" viewBox="0 0 40 30"><path d="M3 16l8-8 9 6 8-8 9 8-10 9-7-5-8 6z" fill="none" stroke="#fff" stroke-width="2.5" stroke-linejoin="round"/></svg></div>
    <div><h3>Platinum Partner</h3><p>Certified on all major software packages including Ledgerline (&amp; Platinum Partner) Tallybook, Sumwise and more. No training required - we can start straight away.</p></div>
  </div>
  <div class="feature" style="top:348px">
    <div class="feature-icon"><svg width="40" height="40" viewBox="0 0 40 40" fill="#888"><circle cx="20" cy="20" r="5"/><circle cx="6" cy="10" r="3.5"/><circle cx="34" cy="10" r="3.5"/><circle cx="6" cy="30" r="3.5"/><circle cx="34" cy="30" r="3.5"/><path d="M6 10L34 30M34 10L6 30" stroke="#888" stroke-width="1.5"/></svg></div>
    <div><h3>Relationship</h3><p>Certified on all major software packages including Ledgerline (&amp; Platinum Partner) Tallybook, Sumwise and more. No training required - we can start straight away.</p></div>
  </div>
  <div class="feature" style="top:500px">
    <div class="feature-icon"><svg width="40" height="28" viewBox="0 0 40 28"><rect x="2" y="3" width="36" height="22" rx="3" fill="none" stroke="#888" stroke-width="2"/><rect x="2" y="8" width="36" height="5" fill="#888"/></svg></div>
    <div><h3>Secure Payment</h3><p>Certified on all major software packages including Ledgerline (&amp; Platinum Partner) Tallybook, Sumwise and more. No training required - we can start straight away.</p></div>
  </div>
  <div class="abs intro-art" role="img" aria-label="Line illustration of accounting documents, charts and calculators arranged in a circle"></div>
</section>

<section class="services">
  <h2 class="abs">How Can We Help?</h2>
  <div class="abs rule"></div>

  <div class="service" style="left:68px;top:190px"><svg width="44" height="50" viewBox="0 0 44 50" fill="none" stroke="#555" stroke-width="2"><rect x="6" y="3" width="32" height="44"/><path d="M14 38v-8M22 38V20M30 38v-12"/></svg><h3>Regular Reporting</h3><p>We can process your accounts from scratch based on bank statements, invoices and bills, keeping you up to date and on track.</p></div>
  <div class="service" style="left:458px;top:190px"><svg width="50" height="50" viewBox="0 0 50 50" fill="none" stroke="#555" stroke-width="2"><circle cx="25" cy="25" r="21"/><circle cx="25" cy="25" r="13"/><path d="M25 18v14M21 21h7M21 29h7"/></svg><h3>Bank Reconciliations</h3><p>We can process your accounts from scratch based on bank statements, invoices and bills, keeping you up to date and on track.</p></div>
  <div class="service" style="left:819px;top:190px"><svg width="44" height="50" viewBox="0 0 44 50" fill="none" stroke="#555" stroke-width="2"><rect x="6" y="3" width="32" height="44"/><path d="M13 15h18M13 23h18M13 31h18M13 39h10"/></svg><h3>Payroll Services</h3><p>We can process your accounts from scratch based on bank statements, invoices and bills, keeping you up to date and on track.</p></div>

  <div class="service" style="left:68px;top:436px"><svg width="50" height="50" viewBox="0 0 50 50" fill="none" stroke="#555" stroke-width="2"><path d="M4 46h42M10 46V32M20 46V24M30 46V28M40 46V14M8 26l12-10 10 6 14-14"/></svg><h3>Regular Reporting</h3><p>We can process your accounts from scratch based on bank statements, invoices and bills, keeping you up to date and on track.</p></div>
  <div class="service" style="left:458px;top:436px"><svg width="54" height="50" viewBox="0 0 54 50" fill="none" stroke="#555" stroke-width="2"><rect x="3" y="4" width="48" height="32"/><path d="M20 46h14M27 36v10"/><circle cx="27" cy="20" r="8"/><path d="M33 26l6 6"/></svg><h3>Accounts Payable &amp; Receivable</h3><p>We can process your accounts from scratch based on bank statements, invoices and bills, keeping you up to date and on track.</p></div>
  <div class="service" style="left:819px;top:436px"><svg width="44" height="50" viewBox="0 0 44 50" fill="none" stroke="#555" stroke-width="2"><rect x="5" y="10" width="34" height="36"/><path d="M14 10V4h16v6M22 20v16M15 29l7 7 7-7"/></svg><h3>Debtor Management</h3><p>We can process your accounts from scratch based on bank statements, invoices and bills, keeping you up to date and on track.</p></div>

  <div class="service" style="left:68px;top:686px"><svg width="50" height="50" viewBox="0 0 50 50" fill="none" stroke="#555" stroke-width="2"><rect x="8" y="4" width="34" height="32"/><path d="M15 13h20M15 20h20M15 27h12M3 44h44M6 36h38l3 8"/></svg><h3>Online Bill Payments</h3><p>We can process your accounts from scratch based on bank statements, invoices and bills, keeping you up to date and on track.</p></div>
  <div class="service" style="left:458px;top:686px"><svg width="54" height="50" viewBox="0 0 54 50" fill="none" stroke="#555" stroke-width="2"><rect x="8" y="10" width="42" height="26"/><rect x="4" y="16" width="42" height="26" fill="#f4f4f4"/><circle cx="25" cy="29" r="6"/></svg><h3>Cash Flow Management</h3><p>We can process your accounts from scratch based on bank statements, invoices and bills, keeping you up to date and on track.</p></div>
  <div class="service" style="left:819px;top:686px"><svg width="44" height="50" viewBox="0 0 44 50" fill="none" stroke="#555" stroke-width="2"><path d="M16 4h12l-4 8h-4zM20 12C6 20 6 46 22 46s16-26 2-34"/><path d="M26 24c-2-2-8-2-8 2s8 2 8 6-6 4-8 2M22 20v4M22 34v4"/></svg><h3>Budgeting</h3><p>We can process your accounts from scratch based on bank statements, invoices and bills, keeping you up to date and on track.</p></div>

  <a class="btn">Start Your Free Trial</a>
</section>

<section class="cta">
  <h2 class="abs">Get in touch and we can fully customise an offering for you</h2>
  <p class="abs">We have offices all over Australia, but even if you aren't near an office we can still help you with your bookkeeping.</p>
  <a class="btn">Start Your Free Trial</a>
</section>

<section class="partners">
  <div class="partner" style="left:100px">Parcelrun</div>
  <div class="partner" style="left:270px">Allhours Gym</div>
  <div class="partner" style="left:443px"><span class="dot"></span>Vanta Promo</div>
  <div class="partner" style="left:615px">Allhours Gym</div>
  <div class="partner" style="left:788px">Parcelrun</div>
  <div class="partner" style="left:955px">Greenroot Supply</div>
</section>

<section class="testimonials">
  <h2 class="abs">What customers are saying about KTR</h2>
  <div class="abs quote-card">
    <div class="abs avatar" role="img" aria-label="Portrait photo of the client"></div>
    <div class="abs person"><div class="name">Marcus Delane</div><div class="role">General Manager</div></div>
    <p class="abs">Marcus was looking for a solution that could be rolled out across various franchises easily. We wanted to make sure his franchisees could focus on running their businesses rather than worrying about admin. At Lumiqor we worked with Marcus to outline a scalable solution that was easy to implement and low maintenance for franchisees - and most importantly, low cost!</p>
  </div>
  <div class="abs video" role="img" aria-label="Promotional video still of a smiling businessman in a suit">
    <div class="abs video-title">Free yourself With KTR We'll do your Bookkeeping.</div>
    <svg class="abs play" width="56" height="56" viewBox="0 0 56 56"><circle cx="28" cy="28" r="27" fill="#8cc63f"/><path d="M22 17l17 11-17 11z" fill="#fff"/></svg>
  </div>
</section>

<section class="contact">
  <div class="abs map" role="img" aria-label="Street map of the office location with a red pin">
    <div class="abs map-label">6/80 Market Lane<br><span style="color:#1a73e8">View larger map</span></div>
    <svg class="abs" style="left:212px;top:110px" width="24" height="34" viewBox="0 0 24 34"><path d="M12 33C4 20 1 16 1 11a11 11 0 0122 0c0 5-3 9-11 22z" fill="#e53935"/><circle cx="12" cy="11" r="4" fill="#a52020"/></svg>
  </div>
  <h2 class="abs">Contact Us</h2>
  <p class="abs intro-text">We have offices all over Australia, but even if you aren't near an office we can still help you with your bookkeeping. Lumiqor Bookkeeping started out in Sydney as Lumiqor Bookkeeping.</p>
  <div class="row" style="top:278px"><span class="label">Address</span><span class="value">14/62 Harbourview Rd Kellyville NSW 2155</span></div>
  <div class="row" style="top:328px"><span class="label">Phone No</span><span class="value">0400 123 456</span></div>
  <div class="row" style="top:368px"><span class="label">Website</span><span class="value">www.ktr-tally.example</span></div>
  <div class="row" style="top:406px"><span class="label">Follow Us</span><span class="social"><span></span><span></span><span></span><span></span></span></div>
</section>

<footer class="site-footer">© Copyright Keystone Tally 2018</footer>

</body>
</html>
```